Online Retailer Needs Banner Ads for Cosmetics Promotion

We are VitaNook.ca, a Canadian Online Retailer for everything Health & Beauty. We will be doing a promotion for 50% off our entire cosmetics category. The full product listing is here:
http://www.vitanook.ca/category/beauty-category
Brands include: Belvane Lyon, Parvis Dublin, Juno, Corraliste, Tavish, Prunet, Glowhaven, and Mira Kettleby.
Our brand colors are white, #81C630 and #302A66, though since this is targeted specifically at cosmetics shoppers, other colors may be used instead.
The ad should feature our logo (attached), the main value proposition for the ad (50% off all cosmetics, coupon code "MAKEUP"), and a call to action at the end (ex. a "Shop Now" button). If it fits the design, another value proposition we use is "Fast Shipping that's Free over $50". Use of animation to keep the ad looking clean is a plus.
The winner will be the ad which is expected to have a higher click through rate.
Output should be in .gif or .swf format. We are looking for banner ads in three sizes: 300x250, 728x90, and 160x600.
Some example of standard ads (<40kb) can be found here:
http://adgallery.quillpathmedia.com/
Specifications for standard ads can be found here:
http://specs.quillpathmedia.com/

```html
<!DOCTYPE html>
<html lang="en">
<head>
<meta charset="utf-8">
<title>VitaNook Cosmetics Banner Set</title>
<link rel="stylesheet" href="https://fonts.googleapis.com/css2?family=Arimo:ital,wght@0,400;0,700;1,700&display=swap">
<style>
  :root {
    --page: #ffffff;
    --green: #6cbe25;
    --green-deep: #2f5d10;
    --orange: #f39a0b;
    --red: #e4261b;
    --red-dark: #a8130c;
    --navy: #1e2c68;
    --lime-text: #d6f27a;
    --ink: #3d3d3d;
    --frame: #9a9a9a;
    --bar: #1b1b1b;
    --header-top: #ffffff;
    --header-bottom: #e4e4e4;
  }
  * { box-sizing: border-box; margin: 0; padding: 0; }
  html, body { width: 1200px; height: 1200px; overflow: hidden; background: var(--page); }
  body { font-family: "Arimo", Arial, sans-serif; }

  .sheet { position: absolute; left: 0; top: 0; width: 860px; height: 860px; transform: scale(1.39535); transform-origin: 0 0; }

  .banner { position: absolute; overflow: hidden; border: 1px solid var(--frame);
    background: linear-gradient(var(--header-top), var(--header-bottom)); }
  .banner svg.shapes { position: absolute; left: 0; top: 0; }
  .size-label { position: absolute; font-size: 15px; color: var(--ink); text-align: center; width: 120px; }

  .logo { position: absolute; display: flex; align-items: center; gap: 4px;
    font-size: 22px; font-weight: 400; color: var(--ink); letter-spacing: -0.5px; }
  .logo-dot { width: 8px; height: 8px; border-radius: 50%; background: var(--green); }

  .coupon { position: absolute; color: #fff; text-align: center; line-height: 1.15; }
  .coupon-label { font-size: 13px; }
  .coupon-code { font-weight: 700; font-style: italic; color: var(--lime-text); font-size: 18px; }

  .offer { position: absolute; color: #fff; font-weight: 700; line-height: 1.05;
    text-shadow: 0 1px 1px rgba(0,0,0,.35); }
  .shipping { position: absolute; color: var(--green-deep); font-weight: 700;
    text-shadow: 0 0 2px #fff, 0 0 2px #fff; }
  .threshold { position: absolute; color: #fff; text-shadow: 0 1px 1px rgba(0,0,0,.3); }
  .threshold strong { font-weight: 700; }

  .deal-tag { position: absolute; background: linear-gradient(var(--red), #c91d10);
    color: #fff; font-weight: 700; text-align: center; border-radius: 3px 12px 12px 3px;
    box-shadow: 0 2px 3px rgba(0,0,0,.3); }

  .products { position: absolute;
    background: linear-gradient(100deg, #e9a0b0 0%, #222 28%, #d8e23a 45%, #f2f2f2 58%, #b2253f 75%, #d9b7b5 100%); }

  .shop-now { position: absolute; display: flex; align-items: center; justify-content: space-between;
    background: linear-gradient(#ff5a4a, var(--red) 55%, #c81a10);
    border-radius: 3px; box-shadow: 0 2px 4px rgba(0,0,0,.35); color: #fff; font-weight: 700; }
  .shop-now .play { border-radius: 50%; background: #5a0c08; border: 2px solid #fff;
    display: flex; align-items: center; justify-content: center; }
  .shop-now .play::after { content: ""; border-left: 9px solid #fff;
    border-top: 6px solid transparent; border-bottom: 6px solid transparent; margin-left: 3px; }
  .hot { position: absolute; background: var(--orange); color: #fff; font-size: 9px;
    font-weight: 700; padding: 1px 8px; transform: rotate(-40deg); }
</style>
</head>
<body>
<main class="sheet">

  <!-- Leaderboard 728x90 -->
  <section class="banner leaderboard" style="left:76px;top:55px;width:728px;height:90px;">
    <svg class="shapes" width="728" height="90" viewBox="0 0 728 90">
      <rect x="0" y="0" width="5" height="90" fill="var(--bar)"/>
      <polygon points="132,0 478,0 455,90 132,90" fill="var(--orange)"/>
      <polygon points="140,0 466,0 445,90 140,90" fill="var(--green)"/>
      <polygon points="134,17 228,17 246,46 228,75 134,75" fill="var(--navy)"/>
    </svg>
    <div class="logo" style="left:10px;top:32px;"><span class="logo-dot"></span>VitaNook</div>
    <div class="coupon" style="left:134px;top:25px;width:100px;">
      <div class="coupon-label" style="font-size:12px;">Coupon Code :</div>
      <div class="coupon-code" style="font-size:17px;">MAKE UP</div>
    </div>
    <div class="offer" style="left:240px;top:10px;font-size:18px;">50% Off all Cosmetics</div>
    <div class="shipping" style="left:241px;top:34px;font-size:18px;">Fast Shipping</div>
    <div class="threshold" style="left:242px;top:57px;font-size:14px;">That free Over <strong style="font-size:20px;">$50</strong></div>
    <div class="deal-tag" style="left:402px;top:54px;width:46px;height:22px;font-size:13px;line-height:22px;transform:rotate(-22deg);">Deal</div>
    <div class="products" role="img" aria-label="Lipstick, mascara and lip gloss product photo" style="left:484px;top:2px;width:130px;height:88px;"></div>
    <div class="hot" style="left:572px;top:34px;">HOT</div>
    <div class="shop-now" style="left:582px;top:30px;width:136px;height:38px;padding:0 6px 0 10px;font-size:13px;">SHOP NOW<span class="play" style="width:28px;height:28px;"></span></div>
  </section>
  <div class="size-label" style="left:354px;top:153px;">728X90</div>

  <!-- Medium rectangle 300x250 -->
  <section class="banner rectangle" style="left:69px;top:292px;width:300px;height:250px;">
    <svg class="shapes" width="300" height="250" viewBox="0 0 300 250">
      <rect x="0" y="0" width="300" height="6" fill="var(--bar)"/>
      <path d="M0,64 Q150,48 300,62 L300,250 L0,250 Z" fill="var(--orange)"/>
      <path d="M0,72 Q150,58 300,70 L300,250 L0,250 Z" fill="var(--red)"/>
      <path d="M0,76 Q80,66 165,64 L152,250 L0,250 Z" fill="var(--green)"/>
      <path d="M172,64 Q240,62 300,70 L300,250 L160,250 Z" fill="#ffffff"/>
      <polygon points="168,14 288,14 288,76 228,100 168,76" fill="var(--navy)"/>
    </svg>
    <div class="logo" style="left:30px;top:22px;font-size:21px;"><span class="logo-dot"></span>VitaNook</div>
    <div class="coupon" style="left:168px;top:30px;width:120px;">
      <div class="coupon-label" style="font-size:14px;">Coupon Code :</div>
      <div class="coupon-code" style="font-size:19px;">MAKE UP</div>
    </div>
    <div class="offer" style="left:8px;top:92px;font-size:21px;">50% Off all<br>Cosmetics</div>
    <div class="shipping" style="left:8px;top:140px;font-size:18px;">Fast Shipping</div>
    <div class="threshold" style="left:8px;top:163px;font-size:14px;">That free Over <strong style="font-size:20px;">$50</strong></div>
    <div class="products" role="img" aria-label="Lipstick, mascara and lip gloss product photo" style="left:188px;top:104px;width:104px;height:146px;"></div>
    <div class="deal-tag" style="left:163px;top:130px;width:50px;height:24px;font-size:14px;line-height:24px;transform:rotate(-22deg);">Deal</div>
    <div class="hot" style="left:0px;top:200px;">HOT</div>
    <div class="shop-now" style="left:10px;top:197px;width:138px;height:38px;padding:0 6px 0 12px;font-size:13px;">SHOP NOW<span class="play" style="width:28px;height:28px;"></span></div>
  </section>
  <div class="size-label" style="left:159px;top:553px;">300X250</div>

  <!-- Skyscraper 160x600 -->
  <section class="banner skyscraper" style="left:635px;top:210px;width:160px;height:600px;">
    <svg class="shapes" width="160" height="600" viewBox="0 0 160 600">
      <rect x="0" y="0" width="160" height="8" fill="var(--bar)"/>
      <path d="M0,88 Q80,72 160,86 L160,322 L80,348 L0,322 Z" fill="var(--orange)"/>
      <path d="M0,96 Q80,82 160,94 L160,314 L80,340 L0,314 Z" fill="var(--red)"/>
      <path d="M0,100 Q80,88 160,98 L160,306 L80,332 L0,306 Z" fill="var(--green)"/>
      <rect x="0" y="352" width="160" height="248" fill="#ffffff"/>
      <polygon points="18,70 142,70 142,122 80,148 18,122" fill="var(--navy)"/>
    </svg>
    <div class="logo" style="left:14px;top:32px;font-size:21px;"><span class="logo-dot"></span>VitaNook</div>
    <div class="coupon" style="left:18px;top:78px;width:124px;">
      <div class="coupon-label" style="font-size:14px;">Coupon Code :</div>
      <div class="coupon-code" style="font-size:19px;">MAKE UP</div>
    </div>
    <div class="offer" style="left:0;top:162px;width:160px;text-align:center;font-size:21px;">50% Off all<br>Cosmetics</div>
    <div class="shipping" style="left:0;top:215px;width:160px;text-align:center;font-size:18px;">Fast Shipping</div>
    <div class="threshold" style="left:0;top:238px;width:160px;text-align:center;font-size:14px;">That free Over<br><strong style="font-size:32px;line-height:40px;">$50</strong></div>
    <div class="deal-tag" style="left:28px;top:362px;width:80px;height:34px;font-size:18px;line-height:34px;transform:rotate(-25deg);">Deal</div>
    <div class="products" role="img" aria-label="Lipstick, mascara and lip gloss product photo" style="left:12px;top:412px;width:140px;height:180px;"></div>
    <div class="hot" style="left:2px;top:556px;">HOT</div>
    <div class="shop-now" style="left:12px;top:550px;width:138px;height:36px;padding:0 6px 0 12px;font-size:13px;">SHOP NOW<span class="play" style="width:28px;height:28px;"></span></div>
  </section>
  <div class="size-label" style="left:655px;top:818px;">160X600</div>

</main>
</body>
</html>
```